business card design for a small scale specialty cut flower farm

We need a business card design for Hollowmere Bloom Farm based in Langley, BC, Canada. We produce specialty, high-end cut flowers and sell locally to florists, local shops and markets and the end user through bouquet subscriptions. The final business card design should be memorable and have a timeless or vintage feel. We would prefer a square shape.
Updates

Target Market(s)

florists, shops and seasonal markets, local flower lovers

Industry/Entity Type

Floral

Contact Information for Business Card

Tamsin Ellery Voss, Grower
Langley, BC, Canada
website: hollowmerebloomfarm.example
instagram: @hollowmerebloomfarm
Tel: 555.317.4290
facebook: www.facebook.example/hollowmereblooms/

Font styles to use
Serif
Decorative
Script

Requirements
Must have
• soft black background colour on front side, the included logo and catch phrase: Fresh Local Seasonal
Nice to have
• phone number and website address on front of card, included photo 6539 incorporated onto the back, possibly photo 6609 as well.

```html
<!DOCTYPE html>
<html lang="en">
<head>
<meta charset="utf-8">
<title>Hollowmere Bloom Farm – Business Card</title>
<link href="https://fonts.googleapis.com/css2?family=Lato:ital,wght@0,300;0,400;0,900;1,300&display=swap" rel="stylesheet">
<style>
  :root {
    --paper: #ffffff;
    --soft-black: #2b2a28;
    --front-ink: #f4f1ec;
    --ink: #1c1c1c;
    --card-green: #507a4c;
    --leaf-light: #b5dba9;
    --leaf-bright: #4caf4a;
    --leaf-mid: #8ec987;
    --bloom-pink: #e9b3d4;
    --bloom-leaf: #4f7f4a;
    --icon-white: #ffffff;
  }
  html, body {
    margin: 0;
    padding: 0;
    width: 1200px;
    height: 548px;
    overflow: hidden;
    background: var(--paper);
  }
  .canvas {
    position: relative;
    width: 1200px;
    height: 548px;
    font-family: "Lato", Arial, sans-serif;
  }
  .card-shapes {
    position: absolute;
    inset: 0;
  }
  .front, .back {
    position: absolute;
    top: 2px;
    width: 543px;
    height: 542px;
  }
  .front { left: 2px; color: var(--front-ink); }
  .back { left: 653px; }

  /* Front: brand */
  .brand-name {
    position: absolute;
    left: 0;
    width: 100%;
    top: 252px;
    margin: 0;
    text-align: center;
    font-weight: 400;
    line-height: 1;
  }
  .brand-name .brand-main {
    display: block;
    font-size: 72px;
  }
  .brand-name .brand-sub {
    display: block;
    margin-top: 12px;
    font-size: 34px;
    letter-spacing: 15px;
    padding-left: 15px;
    text-transform: uppercase;
  }
  .brand-tagline {
    position: absolute;
    left: 0;
    width: 100%;
    top: 392px;
    margin: 0;
    text-align: center;
    font-weight: 300;
    font-style: italic;
    font-size: 25px;
    letter-spacing: 1px;
  }
  .brand-est {
    position: absolute;
    left: 0;
    width: 100%;
    top: 434px;
    margin: 0;
    text-align: center;
    font-weight: 400;
    font-size: 15px;
    letter-spacing: 8px;
    padding-left: 8px;
    box-sizing: border-box;
  }

  /* Back: person and contacts */
  .person-name {
    position: absolute;
    left: 94px;
    top: 50px;
    margin: 0;
    font-weight: 900;
    font-size: 64px;
    line-height: 59px;
    text-transform: uppercase;
    letter-spacing: 0.5px;
  }
  .person-name span { display: block; }
  .name-first { color: var(--leaf-light); }
  .name-middle { color: var(--leaf-bright); }
  .name-last { color: var(--leaf-mid); }
  .person-role {
    position: absolute;
    left: 95px;
    top: 233px;
    margin: 0;
    font-weight: 300;
    font-size: 29px;
    letter-spacing: 1px;
    text-transform: uppercase;
    color: var(--ink);
  }
  .contact {
    position: absolute;
    left: 94px;
    margin: 0;
    font-weight: 400;
    font-size: 26px;
    color: var(--icon-white);
    line-height: 1;
  }
  .contact-phone { top: 328px; font-size: 27px; }
  .contact-instagram { top: 373px; }
  .contact-facebook { top: 420px; }
  .contact-web {
    top: 480px;
    font-size: 23.5px;
    letter-spacing: 1px;
    color: var(--leaf-mid);
  }
</style>
</head>
<body>
<div class="canvas">
  <svg class="card-shapes" width="1200" height="548" viewBox="0 0 1200 548" aria-hidden="true">
    <defs>
      <radialGradient id="bloom-tones" cx="50%" cy="45%" r="60%">
        <stop offset="0%" stop-color="#f3d9e8"/>
        <stop offset="55%" stop-color="var(--bloom-pink)"/>
        <stop offset="100%" stop-color="var(--bloom-leaf)"/>
      </radialGradient>
    </defs>
    <rect class="front-card" x="2" y="2" width="541" height="542" rx="38" fill="var(--soft-black)"/>
    <rect class="back-card" x="653" y="2" width="543" height="542" rx="38" fill="var(--card-green)"/>
    <circle class="social-dot" cx="711" cy="385" r="22.5" fill="var(--icon-white)"/>
    <circle class="social-dot" cx="711" cy="433" r="22.5" fill="var(--icon-white)"/>
    <g class="phone-icon" transform="translate(698 328)" fill="none" stroke="var(--icon-white)" stroke-width="2.4" stroke-linejoin="round">
      <path d="M4 2 h6 l3 7 -4 3 a14 14 0 0 0 7 7 l3 -4 7 3 v6 a2 2 0 0 1 -2 2 A24 24 0 0 1 2 4 a2 2 0 0 1 2 -2 z"/>
    </g>
  </svg>

  <section class="front">
    <svg class="bloom-art" role="img" aria-label="Watercolour illustration of a pink wild rose with green leaves"
         width="232" height="154" viewBox="0 0 232 154" style="position:absolute;left:166px;top:80px">
      <ellipse cx="116" cy="77" rx="114" ry="75" fill="url(#bloom-tones)"/>
    </svg>
    <h1 class="brand-name">
      <span class="brand-main">Hollowmere</span>
      <span class="brand-sub">Bloom Farm</span>
    </h1>
    <p class="brand-tagline">Fresh Local Seasonal</p>
    <p class="brand-est">EST.2019</p>
  </section>

  <section class="back">
    <h2 class="person-name">
      <span class="name-first">Tamsin</span>
      <span class="name-middle">Ellery</span>
      <span class="name-last">Voss</span>
    </h2>
    <p class="person-role">Grower</p>
    <p class="contact contact-phone">(555) 317-4290</p>
    <p class="contact contact-instagram">@hollowmerebloomfarm</p>
    <p class="contact contact-facebook">hollowmereblooms</p>
    <p class="contact contact-web">www.hollowmerebloomfarm.example</p>
  </section>
</div>
</body>
</html>
```